Redesign of page from emergency manual

Please redesign this PDF to look better. Please don't include any stock photos. It must be legible. Making some words bold is probably a good idea.

Here are some things I like :

https://tarrowbooks.com.au/collections/frontpage/products/the-plk-v2-ebook

https://img-cd.vostramediafiles.com/qa-ejkwPLOTYY_SuCKbZNu411Qwgjv8YssPxEdzXN93hDkSRjLXK8WmfgbmrJW4ZZ3yUPK=w1052-h592-rw

```html
<!DOCTYPE html>
<html lang="en">
<head>
<meta charset="utf-8">
<title>Hypertension, Acute</title>
<link rel="stylesheet" href="https://fonts.googleapis.com/css2?family=Noto+Sans:wght@400;700;800;900&family=Poppins:wght@600;700&display=swap">
<style>
  :root {
    --cyan-line: #6ef0fb;
    --cyan-fill: #b3f4fc;
    --ink: #111111;
    --rule-grey: #c4c4c4;
    --paper: #ffffff;
    --backdrop: #eef1f2;
  }
  * { box-sizing: border-box; margin: 0; padding: 0; }
  html, body { width: 1200px; height: 1200px; overflow: hidden; background: var(--backdrop); }
  body { font-family: "Noto Sans", sans-serif; color: var(--ink); }

  .page {
    position: absolute; left: 0; top: 136px;
    width: 1200px; height: 928px;
    background: var(--paper);
  }
  .abs { position: absolute; }

  /* heading */
  .summary-box {
    left: 683px; top: 20px; width: 494px; height: 96px;
    border: 5px solid var(--cyan-line); border-radius: 20px;
    display: flex; align-items: center; justify-content: center;
    padding-left: 14px;
    font-family: "Poppins", sans-serif; font-weight: 700;
    font-size: 17px; line-height: 22px; text-align: center;
  }
  .title-box {
    left: 19px; top: 17px; width: 674px; height: 102px;
    border: 5px solid var(--cyan-line); border-radius: 20px;
    background: var(--paper);
    display: flex; align-items: center; justify-content: center;
  }
  .title {
    font-weight: 900; font-size: 47px; letter-spacing: 1.5px; white-space: nowrap;
  }

  /* intro */
  .intro-bar { left: 56px; top: 150px; width: 4px; height: 97px; background: var(--cyan-line); }
  .intro-text { left: 76px; top: 156px; width: 560px; font-size: 19.5px; line-height: 26px; }
  .checks { left: 54px; top: 252px; width: 580px; font-size: 19.5px; line-height: 25px; list-style: none; }
  .checks li { position: relative; padding-left: 19px; margin-bottom: 17px; }
  .checks li::before {
    content: ""; position: absolute; left: 2px; top: 10px;
    width: 7px; height: 7px; border-radius: 50%; background: var(--ink);
  }
  .checks .sub { display: block; margin-top: 5px; padding-left: 3px; }

  /* range table */
  .range-table {
    left: 646px; top: 169px; width: 496px;
    border-collapse: collapse; font-size: 20px; text-align: center;
  }
  .range-table th, .range-table td { border: 1.5px solid var(--rule-grey); height: 38px; }
  .range-table .range-caption {
    background: var(--cyan-fill); height: 44px;
    font-family: "Poppins", sans-serif; font-weight: 600; font-size: 19px;
  }
  .range-table .col-head { font-weight: 700; }

  /* caution note */
  .caution { left: 52px; top: 396px; width: 1100px; font-size: 19.5px; line-height: 27px; padding-left: 24px; }
  .caution::before { content: "\2217"; position: absolute; left: 0; top: 2px; font-weight: 700; }

  /* drug table */
  .drug-table {
    left: 76px; top: 502px; width: 1058px;
    border-collapse: collapse; font-size: 19.5px; line-height: 24px;
    border-top: 4px solid var(--ink);
  }
  .drug-table th, .drug-table td { border: 1.5px solid var(--ink); vertical-align: top; text-align: left; }
  .drug-table th {
    background: var(--cyan-fill); height: 43px; font-weight: 700;
    text-align: center; padding-top: 3px; font-size: 20px;
  }
  .drug-table .action { width: 238px; padding: 7px 10px; }
  .drug-table .drugs { padding: 7px 10px 7px 14px; }
  .drug-list { list-style: none; }
  .drug-list li { position: relative; padding-left: 25px; margin-bottom: 9px; }
  .drug-list li::before {
    content: ""; position: absolute; left: 0; top: 6px; width: 6px; height: 6px; background: var(--ink);
  }
  .row-1 td { height: 81px; }
  .row-2 td { height: 112px; }
  .row-3 td { height: 76px; }
  .row-4 td { height: 45px; }
</style>
</head>
<body>
<main class="page">
  <div class="abs summary-box">Sustained high blood pressure refractory<br>to treating reversible causes</div>
  <header class="abs title-box"><h1 class="title">HYPERTENSION, ACUTE</h1></header>

  <div class="abs intro-bar"></div>
  <p class="abs intro-text">In pediatrics, hypertension is almost always treated by addressing likely causes such as light anesthesia or measurement error:</p>
  <ul class="abs checks">
    <li>Ensure correct BP cuff size: cuff bladder<br>width ~ 40% of limb circumference</li>
    <li>Ensure arterial line transducer is at level of heart
      <span class="sub">- Consider placing arterial line if not already present</span></li>
  </ul>

  <table class="abs range-table">
    <tr><th class="range-caption" colspan="3">Hypertensive Blood Pressure Range*</th></tr>
    <tr><td class="col-head">Age (yr)</td><td class="col-head">Systolic</td><td class="col-head">Diastolic</td></tr>
    <tr><td>newborn</td><td>&gt;97</td><td>&gt;70</td></tr>
    <tr><td>1-3</td><td>&gt;105</td><td>&gt;61</td></tr>
    <tr><td>4-12</td><td>&gt;113</td><td>&gt;86</td></tr>
  </table>

  <p class="abs caution">Anti-hypertensive drugs are almost never needed for routine pediatric cases. These medications are used almost exclusively for specialized cardiac, neurosurgical, or endocrine (pheochromocytoma) cases. Consult an expert before use. Rule-out increased ICP.</p>

  <table class="abs drug-table">
    <tr><th>Action</th><th>Drug (IV Dosing)</th></tr>
    <tr class="row-1">
      <td class="action">Direct smooth muscle relaxation</td>
      <td class="drugs"><ul class="drug-list">
        <li>Sodium nitroprusside 0.5-10 MICROgrams/kg/min</li>
        <li>HydrALAZINE 0.1-0.2 mg/kg (adult dose 5-10 mg)</li>
      </ul></td>
    </tr>
    <tr class="row-2">
      <td class="action">&beta;-Adrenergic<br>blockade</td>
      <td class="drugs"><ul class="drug-list">
        <li>Esmolol&nbsp; 100-500 MICROgrams/kg over 5 min, then<br>25-300 MICROgrams/kg/min</li>
        <li>Labetalol (also &alpha; effect) 0.2-1 mg/kg q 10 min;&nbsp; 0.4-3 mg/kg/<em>hour</em> (infusion)</li>
      </ul></td>
    </tr>
    <tr class="row-3">
      <td class="action">Calcium channel<br>blockade</td>
      <td class="drugs"><ul class="drug-list">
        <li>niCARdapine&nbsp; 0.5-5 MICROgrams/kg/min</li>
        <li>Clevidipine&nbsp; 0.5-3.5 MICROgrams/kg/min</li>
      </ul></td>
    </tr>
    <tr class="row-4">
      <td class="action">D1-dopamine agonist</td>
      <td class="drugs"><ul class="drug-list">
        <li>Fenoldopam&nbsp; 0.2-0.8 MICROgrams/kg/min</li>
      </ul></td>
    </tr>
  </table>
</main>
</body>
</html>
```